“Chinese small corn" packaging design

we need a packaging design whcih it is for ''small corn". this product is from XISHUANGBANNA in YUNNAN province in south China. some of keys points: the whole packaging colour ONLY use 3 colors, dont exceed more than it; the whole style could be simple and good quality looks like; could be explore more XISHUANGBANNA elements..the product will selling into KA channel, super market, special channel...etc. the key words must be on the front packaging: “4 小时锁鲜" “LOGO name : 岚松嘉坊"..the words of the back of packaging will be providing before confirming finial design..

Target Market(s)

KA, super market, GYM channel, others

Industry/Entity Type

food indurtry

Colors

Designer to choose colors to be used in the design.

Requirements
Must have
• XISHUANGBANNA elements, 4 hours refresh
Nice to have
• look like simple, quality, nutrition,
Should not have
• dont exceed more than 3 colours in whole design

```html
<!DOCTYPE html>
<html lang="zh">
<head>
<meta charset="utf-8">
<title>Small Corn Pack Front</title>
<link href="https://fonts.googleapis.com/css2?family=Arimo:wght@400;700&family=Noto+Sans+SC:wght@400;700&display=swap" rel="stylesheet">
<style>
  :root {
    --bg: #e4e6e9;
    --green: #0f6b35;
    --green-deep: #0a562a;
    --gold: #dcae12;
    --white: #ffffff;
    --label-text: #e8e8e8;
    --photo-light: #f3e3a0;
    --photo-mid: #e2c765;
    --sketch: #3f8a5c;
  }
  html, body {
    margin: 0;
    width: 1200px;
    height: 1200px;
    overflow: hidden;
    background: var(--bg);
  }
  .canvas {
    width: 1200px;
    height: 1200px;
    display: block;
  }
  .brand-cn { font-family: "Noto Sans SC", sans-serif; font-weight: 700; font-size: 40px; fill: var(--white); }
  .brand-en { font-family: "Arimo", sans-serif; font-weight: 400; font-size: 18px; fill: var(--white); }
  .sub-brand { font-family: "Noto Sans SC", sans-serif; font-weight: 400; font-size: 26px; fill: var(--white); }
  .product-name { font-family: "Arimo", sans-serif; font-weight: 700; font-size: 78px; fill: var(--label-text); }
  .freshness { font-family: "Noto Sans SC", sans-serif; font-weight: 400; font-size: 36px; fill: var(--green); }
</style>
</head>
<body>
<svg class="canvas" viewBox="0 0 1200 1200" xmlns="http://www.w3.org/2000/svg">
  <defs>
    <clipPath id="pack-shape">
      <rect x="0" y="0" width="720" height="810" rx="10"/>
    </clipPath>
    <linearGradient id="corn-tones" x1="0" y1="0" x2="1" y2="0">
      <stop offset="0" stop-color="var(--photo-mid)"/>
      <stop offset="0.5" stop-color="var(--photo-light)"/>
      <stop offset="1" stop-color="var(--photo-mid)"/>
    </linearGradient>
  </defs>

  <g class="pack-front" transform="translate(240 195)">
    <g clip-path="url(#pack-shape)">
      <rect class="pack-base" width="720" height="810" fill="var(--white)"/>

      <path class="header-band" d="M0,0 H720 V312 C460,222 230,196 0,282 Z" fill="var(--green)"/>
      <path class="gold-wave" d="M0,282 C230,196 460,222 720,312 V326 C450,262 240,236 0,322 Z" fill="var(--gold)"/>

      <rect class="branch-left" role="img" aria-label="Line sketch of a flowering branch" x="20" y="90" width="210" height="75" rx="30" fill="var(--sketch)" opacity="0.55"/>
      <rect class="branch-right" role="img" aria-label="Line sketch of a flowering branch" x="480" y="112" width="185" height="75" rx="30" fill="var(--sketch)" opacity="0.55"/>
      <rect class="pagoda" role="img" aria-label="Line sketch of a traditional Dai-style pavilion" x="440" y="180" width="165" height="130" fill="var(--sketch)" opacity="0.55"/>

      <g class="brand-lockup">
        <circle cx="260" cy="128" r="22" fill="var(--white)"/>
        <text class="brand-cn" x="298" y="142">青岭农业</text>
        <text class="brand-en" x="302" y="172">Qingling Farms</text>
      </g>
      <text class="sub-brand" x="360" y="210" text-anchor="middle">岚松嘉坊</text>

      <g class="product-window">
        <rect x="184" y="318" width="352" height="342" fill="var(--gold)"/>
        <rect class="corn-photo" role="img" aria-label="Photo of peeled baby corn cobs" x="196" y="330" width="328" height="318" fill="url(#corn-tones)"/>
      </g>

      <path class="name-label" d="M143,440 H577 a10,10 0 0 0 10,10 V545 a10,10 0 0 0 -10,10 H143 a10,10 0 0 0 -10,-10 V450 a10,10 0 0 0 10,-10 Z" fill="var(--green)"/>
      <text class="product-name" x="360" y="525" text-anchor="middle">Small Corn</text>

      <g class="freshness-claim">
        <rect class="corn-icon" role="img" aria-label="Small corn cob icon" x="282" y="690" width="22" height="48" rx="11" fill="var(--gold)"/>
        <text class="freshness" x="312" y="730">4小时锁鲜</text>
      </g>
    </g>
  </g>
</svg>
</body>
</html>
```